Professional Website Design to match new logo for Medical Legal Company

We have rebranded our company and We want a professional but also dynamic web site design for a group of esteemed doctors that provide expert evaluation of an injured worker in a Workers Compensation case.
​
1. Our target market is both the attorneys who select our doctors and any doctors who would wish to join our group.

2. Notes for the Landing Page:
- We prefer a simpler, sleeker more modern look for the landing page.
- We want a simplified landing page with one image, three buttons highlighted in Content document.
- We want the main image to be black and white but it can be splashed with color.
-We think the landing page might be enhanced by add a dark blue or black as a primary color. Of course please feel free to try any color combination you think might work.
- We want "The Meridale Circle" in large letters and "Stewards of a fair and prompt outcome" in small lettering. We don't want icons on the buttons.
- Do not want more than the one picture at top of landing page.
- We do not want any pictures that include faces. Please eliminate or replace. They will not be chosen.
- For the landing page, instead of a second set of photos please experiment with using medical symbols and legal symbols.
​
3. New Company Name: The Meridale Circle
New logo is uploaded bronze and grey/silver will be colors although we are still tweaking the colors for more metallic feel. Want simple not busy.

4. The overall Web page design needs to have some website design effect (e,g image rollover, scrolling effect, hover effect etc).

5. Please follow the attached word document file for the page content of the 4 web pages. Do not mix it up.

Previous company website: www.clinicjuristpanel.example (we wish to convert some of the content from this website to the new brand). Competitor website that we like: www.docboardly.example

Target Market(s)

Professional Elite. Attorneys and Doctors

Industry/Entity Type

Medical Legal

Coding

Coded - Design and coding required

Number of Pages Required

5+ page

Font styles to use
Other font styles liked:
• Helvetica or maybe font that matches logo. We are open

Colors

Designer to choose colors to be used in the design.

Requirements
Must have
• I can't locate on color scale but we want Bronze and Silver/Grey from logo. Additional colors can be added. Various shades of grey
Nice to have
• Black and white photos, simple elegant design
Should not have
• Images with faces of unknown people

```html
<!DOCTYPE html>
<html lang="en">
<head>
<meta charset="utf-8">
<title>The Meridale Circle</title>
<link href="https://fonts.googleapis.com/css2?family=Arimo:wght@400;500;700&family=Marcellus&display=swap" rel="stylesheet">
<style>
:root{
  --bronze:#b8714a;
  --bronze-dark:#7d4a24;
  --bronze-light:#d9895a;
  --ink:#111111;
  --charcoal:#1e1e1e;
  --footer:#1f1f1f;
  --grey-text:#4a4a4a;
  --silver:#c9c9c9;
  --white:#ffffff;
}
*{margin:0;padding:0;box-sizing:border-box}
html,body{width:1200px;height:2306px;overflow:hidden}
body{font-family:"Arimo",Helvetica,Arial,sans-serif;color:var(--ink);background:var(--white);position:relative}
a{color:inherit;text-decoration:none}

/* Hero */
.hero{position:absolute;left:0;top:0;width:1200px;height:523px;overflow:hidden}
.hero-photo{position:absolute;inset:0;background:
  radial-gradient(ellipse at 85% 35%,#6a6a6a 0%,#3f3f3f 35%,transparent 70%),
  radial-gradient(ellipse at 55% 70%,#4a4a4a 0%,transparent 60%),
  linear-gradient(90deg,#262626 0%,#343434 45%,#4b4b4b 100%)}
.nav{position:absolute;left:0;top:0;width:100%;height:72px;border-bottom:1px solid rgba(255,255,255,.18)}
.brand{position:absolute;left:133px;top:22px;display:flex;align-items:center;gap:10px;color:var(--silver);font-family:"Marcellus",serif;font-size:22px;letter-spacing:1px}
.brand-mark{width:16px;height:16px;background:var(--bronze)}
.nav-links{position:absolute;left:545px;top:27px;display:flex;gap:22px;color:var(--white);font-size:14px}
.nav-contact{position:absolute;left:980px;top:18px;width:86px;height:31px;border:1px solid rgba(255,255,255,.8);border-radius:2px;color:var(--white);font-size:14px;display:flex;align-items:center;justify-content:center}
.hero-title{position:absolute;left:133px;top:212px;font-family:"Marcellus",serif;font-size:54px;color:var(--white);letter-spacing:2px;white-space:nowrap}
.hero-tagline{position:absolute;left:133px;top:295px;font-size:16px;color:#e6e6e6}
.hero-rule{position:absolute;left:469px;top:303px;width:268px;height:1px;background:#cfcfcf}
.hero-buttons{position:absolute;left:133px;top:360px;display:flex}
.btn{height:37px;display:flex;align-items:center;justify-content:center;font-size:15px;letter-spacing:.6px;color:var(--white);border:1px solid rgba(255,255,255,.55);background:rgba(0,0,0,.25)}
.btn-stake{width:167px}
.btn-qme{width:177px;margin-left:25px;border-color:var(--bronze-light);background:linear-gradient(90deg,#a4602f,#d98a5b 55%,#b96c3c)}
.btn-member{width:210px;margin-left:24px}
.hero-sub{position:absolute;left:133px;top:411px;font-size:11px;color:#d6d6d6}
.hero-dots{position:absolute;left:1145px;top:255px;display:flex;flex-direction:column;gap:9px}
.hero-dots span{width:8px;height:8px;border:1px solid #bdbdbd;border-radius:50%}
.hero-dots span.active{background:var(--white);border-color:var(--white);height:12px;border-radius:4px}

/* Services */
.eyebrow{position:absolute;left:0;width:1200px;text-align:center;color:var(--bronze);font-size:15px;letter-spacing:3px}
.section-title{position:absolute;left:0;width:1200px;text-align:center;font-weight:700;font-size:33px;color:var(--ink);line-height:1.3}
.services-intro{position:absolute;left:300px;top:701px;width:600px;text-align:center;font-size:13.5px;line-height:20px;color:var(--grey-text)}
.card{position:absolute;top:807px;width:291px;height:320px;border:1px solid var(--bronze);border-radius:3px;text-align:center;padding:32px 36px 0}
.card h3{font-size:20px;line-height:26px;font-weight:700;margin-bottom:15px}
.card p{font-size:11.5px;line-height:18.3px;color:var(--grey-text)}
.card-more{position:absolute;left:0;width:100%;bottom:26px;display:flex;justify-content:center;align-items:center;gap:12px;color:var(--bronze);font-size:15px}
.card-more .dot{width:16px;height:16px;border-radius:50%;background:var(--bronze);display:flex;align-items:center;justify-content:center}
.card-featured{border:none;background:linear-gradient(135deg,#8a4f24 0%,#d6895a 30%,#a25d2f 60%,#7a4820 100%)}
.card-featured h3,.card-featured .card-more{color:var(--white)}
.card-featured p{color:#f1dccd}
.card-featured .card-more .dot{background:var(--white)}

/* Newsletter */
.newsletter{position:absolute;left:0;top:1240px;width:1200px;height:154px;background:linear-gradient(100deg,#2a2a2a 0%,#1c1c1c 50%,#262626 100%)}
.newsletter h2{position:absolute;left:206px;top:52px;color:var(--white);font-size:33px;font-weight:700}
.newsletter-link{position:absolute;left:821px;top:64px;color:var(--bronze);font-size:14px;letter-spacing:1px;display:flex;align-items:center;gap:8px;border-bottom:1px solid var(--bronze);padding-bottom:3px}

/* About */
.about{position:absolute;left:0;top:1394px;width:1200px;height:425px;background:radial-gradient(ellipse at 30% 40%,#e6e6e6 0%,#f3f3f3 45%,#ffffff 80%)}
.about-text{position:absolute;left:370px;top:1590px;width:460px;text-align:center;font-size:13.5px;line-height:20px;color:var(--grey-text)}
.about-btn{position:absolute;left:515px;top:1699px;width:170px;height:38px;border:1px solid var(--bronze);display:flex;align-items:center;justify-content:center;gap:10px;color:var(--bronze);font-size:15px;background:var(--white)}
.about-btn .dot{width:16px;height:16px;border-radius:50%;background:var(--bronze);display:flex;align-items:center;justify-content:center}

/* Footer */
.footer{position:absolute;left:0;top:1819px;width:1200px;height:487px;background:var(--footer);color:#cfcfcf}
.footer .brand{top:72px;font-size:24px}
.footer h4{color:var(--white);font-size:11.5px;font-weight:700;letter-spacing:.3px;position:relative;padding-bottom:9px}
.footer h4::after{content:"";position:absolute;left:0;bottom:0;width:22px;height:1px;background:var(--bronze)}
.hq{position:absolute;left:136px;top:166px;font-size:11.5px;line-height:15px}
.hq h4{margin-bottom:12px}
.hq .accent{color:var(--bronze);font-weight:700;margin-right:6px}
.foot-col{position:absolute;top:75px;font-size:11.5px}
.foot-col h4{margin-bottom:14px}
.foot-col li{list-style:none;height:21.7px}
.foot-rule{position:absolute;left:133px;top:396px;width:934px;height:1px;background:#3a3a3a}
.copyright{position:absolute;left:133px;top:431px;font-size:13px;color:#d0d0d0}
.socials{position:absolute;left:992px;top:430px;display:flex;gap:8px}
.socials span{width:19px;height:19px;border:1px solid var(--bronze);border-radius:50%}
</style>
</head>
<body>

<header class="hero">
  <div class="hero-photo" role="img" aria-label="Black and white photo of a clinician's hands holding a stethoscope, overlaid with faint medical cross and network symbols"></div>
  <nav class="nav">
    <a class="brand" href="#"><span class="brand-mark"></span>MERIDALE</a>
    <div class="nav-links"><a href="#">Home</a><a href="#">Physicians</a><a href="#">Stakeholder</a><a href="#">Meridale Gives Back</a></div>
    <a class="nav-contact" href="#">Contact</a>
  </nav>
  <h1 class="hero-title">The MERIDALE CIRCLE</h1>
  <p class="hero-tagline">Stewards of a fair and prompt outcome</p>
  <div class="hero-rule"></div>
  <div class="hero-buttons">
    <a class="btn btn-stake" href="#">STAKEHOLDERS</a>
    <a class="btn btn-qme" href="#">QME PHYSICIANS</a>
    <a class="btn btn-member" href="#">MEMBER PHYSICIANS</a>
  </div>
  <p class="hero-sub">Attorneys I Carriers I InjuredWorkers</p>
  <div class="hero-dots"><span></span><span></span><span class="active"></span><span></span><span></span></div>
</header>

<section class="services">
  <p class="eyebrow" style="top:584px">SERVICES</p>
  <h2 class="section-title" style="top:607px">What We Do</h2>
  <p class="services-intro">We provide exceptional nationwide service of Medical-Legal Examinations (IME, QME &amp; AME), Peer Reviews, Record Reviews, Functional Capacity Evaluations (FCE), Expert Witness Testimony, and Subsequent Injuries Benefit Trust Fund (SIBTF) eligibility determinations.</p>

  <article class="card" style="left:144px">
    <h3>Expert Source<br>Methodology</h3>
    <p>Our proprietary Expert Source method saves you time, increases your success rate, and gets you answers to complex disputed medical issues. Each year, thousands of attorneys trust our process to get results on over 5,000 cases annually.</p>
    <a class="card-more" href="#">Learn More <span class="dot"><svg width="8" height="8" viewBox="0 0 8 8"><path d="M2 6L6 2M3 2h3v3" stroke="#fff" stroke-width="1.2" fill="none"/></svg></span></a>
  </article>
  <article class="card card-featured" style="left:456px">
    <h3>Extensive<br>Medical Expert<br>Network</h3>
    <p>With over 200 physician in our network, we are sure to have the right expert to have the right expert t meet your needs.All of our physician are highly credentialed and experienced.Our rigorous mentoring, training and creening process ensures that each expert is extremely qualified</p>
    <a class="card-more" href="#">Learn More <span class="dot"><svg width="8" height="8" viewBox="0 0 8 8"><path d="M2 6L6 2M3 2h3v3" stroke="#9a5a2c" stroke-width="1.2" fill="none"/></svg></span></a>
  </article>
  <article class="card" style="left:769px">
    <h3>Medical-Legal<br>Service</h3>
    <p>We offer a wide range ofn services, Independent Medical Examinations (IME),Agreed Medical Evaluation (AME),Qualified Medical Evaluation (QME), Medical Expert Witness Engagements, Records Review, Trial Preparation, Disability Evaluation, Fitness for Duty Evaluation (FEDE) and Medical-Legal Consultation.</p>
    <a class="card-more" href="#">Learn More <span class="dot"><svg width="8" height="8" viewBox="0 0 8 8"><path d="M2 6L6 2M3 2h3v3" stroke="#fff" stroke-width="1.2" fill="none"/></svg></span></a>
  </article>
</section>

<section class="newsletter">
  <h2>Most Recent Newsletter</h2>
  <a class="newsletter-link" href="#"><svg width="14" height="14" viewBox="0 0 14 14"><path d="M7 1v8M4 6l3 3 3-3M1 10v3h12v-3" stroke="#b8714a" stroke-width="1.4" fill="none"/></svg>DOWNLOAD HERE</a>
</section>

<section class="about">
</section>
<p class="eyebrow" style="top:1461px">ABOUT</p>
<h2 class="section-title" style="top:1478px;font-size:33px;line-height:43px">Leaders in Medical<br>Evaluation</h2>
<p class="about-text">The Meridale Circle is a leader in Qualified Medical Evaluations and SIBTF cases in the State of California. Our doctors are dedicated to facilitating settlements through rapid, objective and well researched Expert Medical Opinions</p>
<a class="about-btn" href="#">View Site Map <span class="dot"><svg width="8" height="8" viewBox="0 0 8 8"><path d="M2 6L6 2M3 2h3v3" stroke="#fff" stroke-width="1.2" fill="none"/></svg></span></a>

<footer class="footer">
  <a class="brand" href="#"><span class="brand-mark"></span>MERIDALE</a>
  <div class="hq">
    <h4>HEADQUARTERS</h4>
    <p>2270 Corvell Ave.<br>3rd Floor Brightmoor, CA 90118</p>
    <p style="margin-top:16px"><span class="accent">Call toll free</span>(800) 555-0142</p>
    <p style="margin-top:9px"><span class="accent">Fax</span>(310) 555-0187</p>
  </div>
  <div class="foot-col" style="left:442px">
    <h4>ABOUT</h4>
    <ul><li>Company</li><li>QME Locations</li><li>Privacy Policy</li><li>Careers</li><li>Join Our Network</li><li>Blog</li><li>Exam Request</li><li>FAQ</li><li>Locations</li><li>Login To Your Account</li></ul>
  </div>
  <div class="foot-col" style="left:633px">
    <h4>EDUCATION</h4>
    <ul><li>Live Seminar QME</li><li>Report Writing Course</li><li>Online QME Report</li><li>Writing Course</li><li>QME Continuing</li><li>Education (CEU)</li><li>AMA Guides 6th Edition</li><li>IME Training</li></ul>
  </div>
  <div class="foot-col" style="left:842px">
    <h4>SERVICES</h4>
    <ul><li>IME</li><li>AME</li><li>QME</li><li>Subsequent Injuries Fund</li><li>Ergonomic Evaluations</li><li>Measuring Workers</li><li>Pre-Employment Screenings</li><li>Fit for Duty</li><li>Functional Capacity Evaluation</li><li>FCE, ACOEM &amp; ODG</li><li>Physician's Guide</li><li>Impairment Rating</li></ul>
  </div>
  <div class="foot-rule"></div>
  <p class="copyright">Copyright © 2024 I Clinic Jurist Panel</p>
  <div class="socials"><span></span><span></span><span></span></div>
</footer>

</body>
</html>
```